Postcard Design

I am an attorney and have my own law firm, Law Offices of Gregory T. Halvorsen. My address is 4582 Canterbury Parkway, #318, Glen Burnie, MD 21061. (410) 555-0187. E-mail gthlegal@fernmail.example.

I want to design two full color postcards, I think the size is about 8.5 by 5.5.

The first is attact Driving While Suspended and Driving Without Insurance client's. I have a list of people charged with those crimes and the postcard goes out each week.

I have been sending letters for years and have been successful but am looking to send only postcards. I am very good at writing the message, terrible with art work. I need you to place the information that I provide below onto a post card with the idea that all of those that receive it will call me. Each person charged receives about 5 postcards and 10 letters from lawyers. No other lawyer advertises just Driving While Suspended and Driving Without Insurance, they all advertise DUI/DWI and other types. My goal is for the client to see my postcard and say "I might as well throw the other stuff away because this is the guy who can do my case well for a great price."

Here are the words that I want on the postcard. Some large, some small. Artwork and good coloring a must, that's what I need help with. Need to use both sides and leave only room for address label and stamp.

DRIVING SUSPENDED AND DRIVING WITHOUT INSURANCE $395.00 FLAT FEE.....INCLUDES ALL UNDERLYING CHARGES!

I have have handled over 5000 cases in AA County and Howard County for more than 22 years. I know the Judges, they know me. There is NO reason to spend omre than $395.00 for a first offense driving suspended or driving without insurance. Should you have a lawyer? Yes, nobody should go to court alone. Should you call me? Over 5000 satisfied client's would say so.

MANY CASES DISMISSED BEFORE COURT!

MONEY BACK GUARANTEE......YOU WILL NOT GET POINTS ON YOUR LICENSE FOR YOUR FIRST OFFENSE DRIVING SUSPENDED OR DRIVING WITHOUT INSURANCE. IF YOU DO, I WILL REFUND YOUR ENTIRE FEE!

Law Offices of Gregory T. Halvorsen

Gregory T. Halvorsen, Traffic Defense Attorney

FREE CONSULTATION, PHONES ANSWERED 24/7

HOLLOWAY CREST BUILDING
4582 Canterbury Parkway, #318
Glen Burnie, MD 21061

(410) 555-0187

APPOINTMENTS AVAILABLE DAY, EVENING AND WEEKENDS

Industry/Entity Type

Attorney

Requirements
Must have
• The ad must also include small language on each side of the postcard that says "this is an advertisement"

```html
<!DOCTYPE html>
<html lang="en">
<head>
<meta charset="utf-8">
<title>Driving While Suspended Postcard – Law Offices of Gregory T. Halvorsen</title>
<link rel="stylesheet" href="https://fonts.googleapis.com/css2?family=Open+Sans:wght@400;600;700;800&family=Cinzel:wght@400;500&display=swap">
<style>
  :root {
    --gold: #f7b519;
    --amber: #f6a61b;
    --charcoal: #3a3a3c;
    --navy: #0e3a6b;
    --navy-deep: #082a52;
    --band-blue: #1d5e96;
    --alert-red: #e1261f;
    --ink: #050505;
    --white: #ffffff;
    --muted: #a9a9a9;
  }
  html, body { margin: 0; padding: 0; overflow: hidden; background: #ffffff; }
  .postcard {
    position: relative;
    width: 1200px;
    height: 924px;
    overflow: hidden;
    background: var(--ink);
    font-family: "Open Sans", Arial, sans-serif;
  }
  .service-area {
    position: absolute; left: 0; top: 0; width: 1200px; height: 146px;
    background: var(--gold);
    color: var(--charcoal);
    text-align: center;
    font-weight: 700;
    line-height: 1;
  }
  .service-area .line-one { position: absolute; top: 26px; width: 100%; font-size: 55px; letter-spacing: -0.5px; }
  .service-area .line-two { position: absolute; top: 84px; width: 100%; font-size: 55px; letter-spacing: -0.5px; }
  .service-area .small-word { font-size: 38px; }
  .tagline-band {
    position: absolute; left: 0; top: 146px; width: 1200px; height: 50px;
    background: linear-gradient(180deg, var(--band-blue), #0f3d6e);
    color: var(--white);
    text-align: center;
    font-size: 27px; line-height: 50px; letter-spacing: 3.4px;
  }
  .road-photo {
    position: absolute; left: 0; top: 196px; width: 1200px; height: 406px;
    background:
      radial-gradient(ellipse 220px 160px at 700px 320px, rgba(220,230,235,0.55), transparent 70%),
      radial-gradient(ellipse 500px 260px at 620px 80px, rgba(120,170,60,0.8), transparent 75%),
      linear-gradient(160deg, #0c1a10 0%, #2f5a22 35%, #49772c 55%, #3b4a4a 75%, #1a2228 100%);
  }
  .speedometer-photo {
    position: absolute; left: 690px; top: 602px; width: 510px; height: 322px;
    background:
      radial-gradient(ellipse 120px 160px at 150px 140px, rgba(255,80,20,0.85), rgba(180,30,10,0.5) 45%, transparent 75%),
      radial-gradient(ellipse 300px 200px at 330px 90px, rgba(90,110,130,0.45), transparent 75%),
      var(--ink);
  }
  .headline {
    position: absolute; left: 68px; top: 206px;
    color: var(--white); font-weight: 700; font-size: 77px; line-height: 1; letter-spacing: -1px;
    margin: 0;
  }
  .subhead {
    position: absolute; left: 68px; top: 298px;
    color: var(--amber); font-weight: 700; font-size: 64px; line-height: 64px; letter-spacing: -0.5px;
    margin: 0;
  }
  .price {
    position: absolute; left: 68px; top: 436px;
    color: var(--amber); font-weight: 700; white-space: nowrap; line-height: 1;
  }
  .price .currency { font-size: 30px; vertical-align: 0; }
  .price .amount { font-size: 80px; letter-spacing: -1px; }
  .price .cents { font-size: 30px; vertical-align: 40px; margin-left: -2px; }
  .price .fee-label { font-size: 42px; margin-left: 20px; vertical-align: 8px; }
  .includes {
    position: absolute; left: 68px; top: 526px;
    color: var(--white); font-weight: 700; font-size: 22px; line-height: 1;
  }
  .firm-card {
    position: absolute; left: 832px; top: 314px; width: 368px; height: 234px;
    background: var(--navy);
    color: var(--white);
    font-family: "Cinzel", "Times New Roman", serif;
    padding: 16px 0 0 22px; box-sizing: border-box;
  }
  .firm-card .firm-name { font-size: 34px; line-height: 40px; margin: 0; font-weight: 400; }
  .firm-card .firm-owner { font-size: 19px; line-height: 30px; margin: 0; letter-spacing: 0.5px; }
  .firm-card .rule { width: 316px; height: 3px; background: var(--white); margin: 12px 0 10px; }
  .firm-card .attorney { font-size: 21px; line-height: 30px; margin: 0; letter-spacing: 0.5px; }
  .dismissed-badge {
    position: absolute; left: 287px; top: 572px; width: 626px; height: 44px;
    background: var(--alert-red);
    border: 3px dotted var(--white);
    box-sizing: border-box;
    outline: 3px solid var(--alert-red);
    color: var(--white); text-align: center;
    font-size: 22px; line-height: 38px; letter-spacing: 1.2px;
  }
  .ad-disclaimer {
    position: absolute; left: 36px; top: 880px;
    transform: rotate(-90deg); transform-origin: 0 0;
    color: var(--muted); font-size: 11px; letter-spacing: 1.2px; white-space: nowrap;
  }
  .brace { position: absolute; top: 645px; width: 46px; height: 230px; }
  .brace.left { left: 88px; }
  .brace.right { left: 686px; }
  .guarantee {
    position: absolute; left: 128px; top: 652px; width: 556px;
    color: var(--amber); text-align: center;
  }
  .guarantee h2 { margin: 0 0 6px; font-size: 29px; font-weight: 700; line-height: 36px; }
  .guarantee p { margin: 0; font-size: 22px; line-height: 33px; }
  .guarantee .refund { margin-top: 10px; font-weight: 700; line-height: 32px; }
  .call-to-action {
    position: absolute; left: 730px; top: 760px; width: 440px;
    text-align: center; font-weight: 700; line-height: 1;
  }
  .call-to-action .call-today { color: var(--white); font-size: 29px; }
  .call-to-action .phone { color: var(--gold); font-size: 50px; margin-top: 12px; letter-spacing: 1px; }
  .call-to-action .consult { color: var(--gold); font-size: 24px; margin-top: 16px; }
</style>
</head>
<body>
<main class="postcard">
  <header class="service-area">
    <div class="line-one">SERVING ANNE ARUNDEL, HOWARD</div>
    <div class="line-two"><span class="small-word">AND</span> BALTIMORE COUNTIES</div>
  </header>
  <div class="tagline-band">OUTSTANDING AND AFFORDABLE LEGAL REPRESENTATION</div>

  <div class="road-photo" role="img" aria-label="Motion-blurred photo of a winding road through a green tree-lined tunnel"></div>
  <div class="speedometer-photo" role="img" aria-label="Close-up photo of a glowing red-orange car speedometer and tachometer"></div>

  <h1 class="headline">DRIVING WHILE SUSPENDED</h1>
  <h2 class="subhead">DRIVING WITHOUT<br>INSURANCE</h2>
  <div class="price"><span class="currency">$</span><span class="amount">395.</span><span class="cents">00</span><span class="fee-label">FLAT FEE</span></div>
  <div class="includes">INCLUDES ALL UNDERLYING CHARGES!</div>

  <section class="firm-card">
    <p class="firm-name">Law Offices</p>
    <p class="firm-owner">of Gregory T. Halvorsen</p>
    <div class="rule"></div>
    <p class="attorney">Gregory T. Halvorsen,<br>Traffic Defense<br>Attorney</p>
  </section>

  <div class="dismissed-badge">MANY CASES DISMISSED BEFORE COURT!</div>

  <div class="ad-disclaimer">THIS IS AN ADVERTISEMENT</div>

  <svg class="brace left" viewBox="0 0 46 230" aria-hidden="true">
    <path d="M40 4 C18 6 20 30 20 60 L20 92 C20 108 14 113 4 115 C14 117 20 122 20 138 L20 170 C20 200 18 224 40 226" fill="none" stroke="var(--amber)" stroke-width="6" stroke-linecap="round"/>
  </svg>
  <svg class="brace right" viewBox="0 0 46 230" aria-hidden="true">
    <path d="M6 4 C28 6 26 30 26 60 L26 92 C26 108 32 113 42 115 C32 117 26 122 26 138 L26 170 C26 200 28 224 6 226" fill="none" stroke="var(--amber)" stroke-width="6" stroke-linecap="round"/>
  </svg>

  <section class="guarantee">
    <h2>MONEY BACK GUARANTEE</h2>
    <p>You will not get points on your license for<br>your first offense driving while suspended or<br>driving without insurance.</p>
    <p class="refund">IF YOU DO, I WILL REFUND<br>YOUR ENTIRE FEE!</p>
  </section>

  <section class="call-to-action">
    <div class="call-today">CALL TODAY!</div>
    <div class="phone">(410) 555-0187</div>
    <div class="consult">Call 24/7 FREE CONSULTATION</div>
  </section>
</main>
</body>
</html>
```